Tech business card design

We need an amazing business card design for our new business 'Brakka' a marketing tech startup based in Sydney, Australia. We provide an online marketplace for businesses to search and buy advertising media, connect with service providers and learn more about marketing. We wish to communicate 'cool tech', reliability and professionalism and design based around our logo.

Target Market(s)

Business Owners

Contact Information for Business Card

Name
Position
Email Address
Website
Phone Number

Font styles to use
Other font styles liked:
• Avenir & Avenir Next

Colors

Designer to choose colors to be used in the design.

```html
<!DOCTYPE html>
<html lang="en">
<head>
<meta charset="UTF-8">
<title>Brakka Business Card</title>
<link href="https://fonts.googleapis.com/css2?family=Nunito+Sans:wght@400;600;800;900&display=swap" rel="stylesheet">
<style>
  :root {
    --stage: #17181a;
    --card: #25272a;
    --ink: #f2f3f5;
    --ink-soft: #b9bcc2;
    --front-mark: #3b3e43;
    --rule: #d9dbe0;
  }
  * { margin: 0; padding: 0; box-sizing: border-box; }
  html, body { width: 1200px; height: 800px; overflow: hidden; }
  body {
    background: var(--stage);
    font-family: "Nunito Sans", "Avenir Next", Avenir, sans-serif;
    color: var(--ink);
    display: flex;
    align-items: center;
    justify-content: center;
    gap: 48px;
  }
  .card {
    position: relative;
    width: 525px;
    height: 300px;
    border-radius: 18px;
    background: var(--card);
    box-shadow: 0 14px 34px rgba(0,0,0,.45);
    overflow: hidden;
  }

  /* Front */
  .card-front {
    display: flex;
    flex-direction: column;
    align-items: center;
    justify-content: center;
  }
  .front-wordmark {
    font-size: 92px;
    font-weight: 900;
    letter-spacing: -2px;
    line-height: 1;
    color: var(--front-mark);
  }
  .front-website {
    margin-top: 14px;
    font-size: 13px;
    letter-spacing: 6px;
    color: var(--ink);
  }

  /* Back */
  .back-wordmark {
    position: absolute;
    top: 34px;
    right: 36px;
    font-size: 64px;
    font-weight: 900;
    letter-spacing: -1.5px;
    line-height: 1;
    color: var(--ink);
  }
  .back-rule {
    position: absolute;
    left: 130px;
    right: 36px;
    top: 128px;
    height: 1px;
    background: var(--rule);
  }
  .contact-rule {
    position: absolute;
    left: 36px;
    width: 150px;
    top: 206px;
    height: 1px;
    background: var(--rule);
  }
  .edge-dot {
    position: absolute;
    left: -14px;
    top: 64px;
    width: 30px;
    height: 30px;
    border-radius: 50%;
    background: var(--ink);
  }
  .holder {
    position: absolute;
    left: 36px;
    top: 58px;
  }
  .holder-name {
    font-size: 19px;
    font-weight: 400;
    line-height: 1.15;
  }
  .holder-name strong { font-weight: 800; }
  .holder-role {
    font-size: 14px;
    color: var(--ink-soft);
  }
  .address {
    position: absolute;
    right: 36px;
    top: 146px;
    font-size: 14px;
    line-height: 1.35;
    text-align: left;
  }
  .contact-list {
    position: absolute;
    left: 36px;
    top: 216px;
    list-style: none;
    font-size: 13.5px;
    line-height: 1.55;
  }
  .contact-list li { display: flex; align-items: center; gap: 8px; }
  .contact-icon { width: 14px; height: 14px; flex: none; }
</style>
</head>
<body>

  <section class="card card-front" aria-label="Business card front">
    <div class="front-wordmark">Brakka</div>
    <div class="front-website">www.brakkaweb.com</div>
  </section>

  <section class="card card-back" aria-label="Business card back">
    <span class="edge-dot"></span>
    <div class="holder">
      <div class="holder-name">Liam <strong>Carter</strong></div>
      <div class="holder-role">Manager</div>
    </div>

    <div class="back-wordmark">Brakka</div>
    <div class="back-rule"></div>

    <address class="address" style="font-style:normal">
      PO BOX 456, Harbour Lane<br>
      9th street Sydney<br>
      Australia
    </address>

    <div class="contact-rule"></div>
    <ul class="contact-list">
      <li>
        <svg class="contact-icon" viewBox="0 0 16 16" aria-hidden="true">
          <circle cx="8" cy="8" r="7.5" fill="#f2f3f5"/>
          <path d="M5.2 4.2l1.4-.2.8 2-1 .8a5 5 0 0 0 2.8 2.8l.8-1 2 .8-.2 1.4c-3.6.4-7-3-6.6-6.6z" fill="#25272a"/>
        </svg>
        555.210.4478
      </li>
      <li>
        <svg class="contact-icon" viewBox="0 0 16 16" aria-hidden="true">
          <circle cx="8" cy="8" r="7.5" fill="#f2f3f5"/>
          <rect x="4" y="5" width="8" height="6" rx="1" fill="#25272a"/>
          <path d="M4.4 5.6L8 8.4l3.6-2.8" stroke="#f2f3f5" stroke-width=".9" fill="none"/>
        </svg>
        hello@brakkamail.com
      </li>
      <li>
        <svg class="contact-icon" viewBox="0 0 16 16" aria-hidden="true">
          <circle cx="8" cy="8" r="7.5" fill="#f2f3f5"/>
          <g stroke="#25272a" stroke-width=".9" fill="none">
            <circle cx="8" cy="8" r="4"/>
            <ellipse cx="8" cy="8" rx="1.7" ry="4"/>
            <path d="M4 8h8"/>
          </g>
        </svg>
        www.brakkaweb.com
      </li>
    </ul>
  </section>

</body>
</html>
```